Exciting new Aussie social network app - designer wanted!

Interested in this entire Freelance Job?
Here is the full project link:
http://jobs.pixelquarry.com.au/job.aspx?id=582716
****
We are a startup based in Melbourne working on a hot new iOS/Android social media app with an edge.
We have completed the scoping phase with the app developers and we are currently seeking a talented app UI/UX designer to work with to create something highly polished.
Our aim with this competition is to mockup the first screen of our app and effectively meet the designer we would love to move forward with to complete the entire design phase after a full debrief. Our app will be comparable to the look/feel of the Quillmoss or Glimmerdot apps, however, the functionality will be a little different. One of our app's main features does involve sharing smartphone captured photos to a stream (stylised gallery of photos) on a network.
We are inspired by the design language of the following iOS apps:
Quillmoss
https://apps.velmora.example/au/app/quillmoss/id813560274?mt=8
Barvo
https://apps.velmora.example/au/app/barvo/id690134827?mt=8
Hoxwelt
https://apps.velmora.example/au/app/hoxwelt/id731842056?mt=8
Lumbrazet
https://apps.velmora.example/au/app/lumbrazet/id572019386?mt=8
Please refer to the screenshot attached entitled MAIN SCREEN and create your own version of this UI/UX for this competition.
Our requirements -
* The title at the top title bar is called "Zorvy"
* the 5 navigation text & buttons at the bottom dock from left to right are:
FEED (Icon of a map pin drop), PEOPLE (Icon of 3 people), CAMERA graphic or a PLUS (+) symbol or both without text label, ACTIVITY(chat boxes/hearts), ME (Icon of Person)
* We need to see what the dock items would like like in each of the 5 states. Eg. What would it look like then the FEED state is highlighted when the user is in the feed section of the app.
* Screen to display whether you are following these users or displaying content from all users.
* We want a small text overlay over each image in the corner, perhaps semi-transparent, to show a 3-4 character code and a heart symbol to like the image.
* We need to see at least 1 new notification any of the dock items
Please refer to attached files for further illustration of buttons we have considered.
Thank you very much for your effort!
We look forward to your mockup and hopefully further work together!
If you are interested in this entire job check out our link to the full freelance project:
Target Market(s)
18-35 years, we expect a more female user demographic, but want to appeal to both sexes.
Industry/Entity Type
Camera
Look and feel

```html
<!DOCTYPE html>
<html lang="en">
<head>
<meta charset="utf-8">
<title>Zorvy – People screen</title>
<link rel="stylesheet" href="https://fonts.googleapis.com/css2?family=Open+Sans:wght@400;600;700;800&display=swap">
<style>
  :root {
    --stage: #8f9a9a;
    --brand-red: #c8100a;
    --accent-red: #e0241c;
    --status-black: #0c0c0c;
    --bar-dark: #2f3031;
    --dock-dark: #2e2f30;
    --grid-grey: #8a9494;
    --tile-frame: #ffffff;
    --muted-text: #9a9c9d;
    --dock-text: #a3a5a6;
    --ring-grey: #55585a;
    --badge-bg: rgba(30, 30, 30, 0.72);
    --white: #ffffff;
  }
  * { box-sizing: border-box; margin: 0; padding: 0; }
  html, body { width: 699px; height: 1200px; overflow: hidden; }
  body {
    background: var(--stage);
    font-family: "Open Sans", Arial, sans-serif;
    position: relative;
  }
  .app-screen {
    position: absolute;
    left: 51px; top: 154px;
    width: 596px; height: 892px;
    overflow: hidden;
    background: var(--grid-grey);
  }
  /* status bar */
  .status-bar {
    position: absolute; left: 0; top: 0; width: 100%; height: 31px;
    background: var(--status-black);
    color: var(--white);
    font-size: 20px; font-weight: 600;
    display: flex; align-items: center;
  }
  .status-left { position: absolute; left: 8px; display: flex; align-items: center; gap: 6px; }
  .signal { display: flex; align-items: flex-end; gap: 2px; height: 12px; }
  .signal span { display: block; width: 3px; background: var(--white); }
  .signal span.off { height: 2px !important; background: #777; }
  .carrier-net { margin-left: 10px; font-size: 18px; }
  .status-time { position: absolute; left: 0; right: 0; text-align: center; }
  .status-right { position: absolute; right: 8px; display: flex; align-items: center; gap: 8px; }
  .battery { width: 36px; height: 16px; border: 2px solid var(--white); border-radius: 3px; padding: 2px; position: relative; }
  .battery::after { content: ""; position: absolute; right: -5px; top: 4px; width: 3px; height: 5px; background: var(--white); }
  .battery-level { width: 95%; height: 100%; background: var(--white); }

  /* header */
  .title-bar {
    position: absolute; left: 0; top: 31px; width: 100%; height: 69px;
    background: var(--brand-red);
  }
  .menu-button { position: absolute; left: 24px; top: 24px; width: 36px; height: 22px; }
  .menu-button span { display: block; height: 4px; border-radius: 2px; background: var(--white); margin-bottom: 5px; }
  .app-name {
    position: absolute; left: 0; right: 0; top: 10px;
    text-align: center; color: var(--white);
    font-size: 42px; font-weight: 800; letter-spacing: 1px; line-height: 50px;
  }

  /* tabs */
  .feed-tabs {
    position: absolute; left: 0; top: 100px; width: 100%; height: 68px;
    background: var(--bar-dark);
    display: flex;
  }
  .feed-tab {
    flex: 1; text-align: center; line-height: 64px;
    font-size: 23px; color: var(--muted-text); position: relative;
  }
  .feed-tab.is-active { color: var(--accent-red); }
  .feed-tab.is-active::after {
    content: ""; position: absolute; left: 0; right: 0; bottom: 0; height: 5px; background: var(--accent-red);
  }

  /* grid */
  .photo-grid { position: absolute; left: 0; top: 168px; width: 100%; height: 625px; overflow: hidden; }
  .photo-tile {
    position: absolute; width: 185px; height: 168px;
    border: 3px solid var(--tile-frame);
  }
  .photo-fill { position: absolute; inset: 0; }
  .like-badge {
    position: absolute; right: 0; top: 0;
    width: 70px; height: 30px;
    background: var(--badge-bg);
    border-left: 3px solid var(--tile-frame); border-bottom: 3px solid var(--tile-frame);
    color: var(--white); font-size: 17px;
    display: flex; align-items: center; justify-content: center; gap: 4px;
  }
  .like-badge svg { width: 17px; height: 15px; }

  /* dock */
  .dock {
    position: absolute; left: 0; bottom: 0; width: 100%; height: 99px;
    background: var(--dock-dark);
  }
  .dock-item {
    position: absolute; top: 0; width: 112px; height: 99px;
    text-align: center; color: var(--dock-text); font-size: 19px;
  }
  .dock-item svg { position: absolute; left: 50%; top: 18px; transform: translateX(-50%); }
  .dock-label { position: absolute; left: 0; right: 0; top: 62px; }
  .dock-item.is-active { color: var(--accent-red); }
  .dock-item.is-active::before {
    content: ""; position: absolute; left: 0; right: 0; top: -6px; height: 6px; background: var(--accent-red);
  }
  .camera-button {
    position: absolute; left: 223px; top: 778px;
    width: 150px; height: 150px; border-radius: 50%;
    background: var(--dock-dark);
    border: 3px solid var(--ring-grey);
  }
  .camera-button svg { position: absolute; left: 50%; top: 38px; transform: translateX(-50%); }
  .notice-badge {
    position: absolute; left: 547px; top: 778px;
    width: 30px; height: 30px; border-radius: 50%;
    background: var(--accent-red); color: var(--white);
    font-size: 16px; font-weight: 700; text-align: center; line-height: 30px;
  }
</style>
</head>
<body>
<main class="app-screen">
  <div class="status-bar">
    <div class="status-left">
      <div class="signal"><span style="height:4px"></span><span style="height:6px"></span><span class="off"></span><span class="off"></span><span class="off"></span></div>
      <span>Corvana</span><span class="carrier-net">3G</span>
    </div>
    <div class="status-time">6:42 PM</div>
    <div class="status-right"><span>95%</span><div class="battery"><div class="battery-level"></div></div></div>
  </div>

  <header class="title-bar">
    <div class="menu-button"><span></span><span></span><span></span></div>
    <h1 class="app-name">ZORVY</h1>
  </header>

  <nav class="feed-tabs">
    <div class="feed-tab">All Users</div>
    <div class="feed-tab is-active">Following</div>
  </nav>

  <section class="photo-grid">
    <div class="photo-tile" style="left:10px;top:10px"><div class="photo-fill" role="img" aria-label="Portrait of a user with graphic face paint" style="background:linear-gradient(135deg,#9a9a98,#3b3b3b)"></div><div class="like-badge">123<svg viewBox="0 0 24 21"><path d="M12 21 2 11A6 6 0 0 1 12 3a6 6 0 0 1 10 8z" fill="#e0241c"/></svg></div></div>
    <div class="photo-tile" style="left:205px;top:10px"><div class="photo-fill" role="img" aria-label="Portrait of a user with dark hair" style="background:linear-gradient(135deg,#3a2a24,#c79a86 55%,#2a1c18)"></div><div class="like-badge">123<svg viewBox="0 0 24 21"><path d="M12 21 2 11A6 6 0 0 1 12 3a6 6 0 0 1 10 8z" fill="#e0241c"/></svg></div></div>
    <div class="photo-tile" style="left:401px;top:10px"><div class="photo-fill" role="img" aria-label="Portrait of a user with long red hair" style="background:linear-gradient(135deg,#e0a25a,#a5461c 55%,#5a1e0c)"></div><div class="like-badge">123<svg viewBox="0 0 24 21"><path d="M12 21 2 11A6 6 0 0 1 12 3a6 6 0 0 1 10 8z" fill="#e0241c"/></svg></div></div>

    <div class="photo-tile" style="left:10px;top:191px"><div class="photo-fill" role="img" aria-label="Portrait of a user with long dark hair" style="background:linear-gradient(135deg,#e4e4e4,#6a5048 55%,#2a2020)"></div><div class="like-badge">123<svg viewBox="0 0 24 21"><path d="M12 21 2 11A6 6 0 0 1 12 3a6 6 0 0 1 10 8z" fill="#e0241c"/></svg></div></div>
    <div class="photo-tile" style="left:205px;top:191px"><div class="photo-fill" role="img" aria-label="Close portrait of a user" style="background:linear-gradient(135deg,#2a2626,#b98c78 60%,#3a2c28)"></div><div class="like-badge">123<svg viewBox="0 0 24 21"><path d="M12 21 2 11A6 6 0 0 1 12 3a6 6 0 0 1 10 8z" fill="#e0241c"/></svg></div></div>
    <div class="photo-tile" style="left:401px;top:191px"><div class="photo-fill" role="img" aria-label="Portrait of a user outdoors" style="background:linear-gradient(135deg,#c9d6d8,#b38a6a 55%,#6a4a32)"></div><div class="like-badge">123<svg viewBox="0 0 24 21"><path d="M12 21 2 11A6 6 0 0 1 12 3a6 6 0 0 1 10 8z" fill="#e0241c"/></svg></div></div>

    <div class="photo-tile" style="left:10px;top:373px"><div class="photo-fill" role="img" aria-label="Portrait of a user against greenery" style="background:linear-gradient(135deg,#b8c27a,#c89a84 55%,#4a2e24)"></div><div class="like-badge">123<svg viewBox="0 0 24 21"><path d="M12 21 2 11A6 6 0 0 1 12 3a6 6 0 0 1 10 8z" fill="#e0241c"/></svg></div></div>
    <div class="photo-tile" style="left:205px;top:373px"><div class="photo-fill" role="img" aria-label="Fashion portrait of a user in black" style="background:linear-gradient(135deg,#1a1a1e,#8a6a72 50%,#121214)"></div><div class="like-badge">123<svg viewBox="0 0 24 21"><path d="M12 21 2 11A6 6 0 0 1 12 3a6 6 0 0 1 10 8z" fill="#e0241c"/></svg></div></div>
    <div class="photo-tile" style="left:401px;top:373px"><div class="photo-fill" role="img" aria-label="Fashion portrait of a user in a studio" style="background:linear-gradient(135deg,#e6d8c8,#b48c6a 55%,#3a2c24)"></div><div class="like-badge">123<svg viewBox="0 0 24 21"><path d="M12 21 2 11A6 6 0 0 1 12 3a6 6 0 0 1 10 8z" fill="#e0241c"/></svg></div></div>

    <div class="photo-tile" style="left:10px;top:554px"><div class="photo-fill" role="img" aria-label="Portrait of a blonde user" style="background:linear-gradient(135deg,#f0d8dc,#e2c0a8)"></div><div class="like-badge">123<svg viewBox="0 0 24 21"><path d="M12 21 2 11A6 6 0 0 1 12 3a6 6 0 0 1 10 8z" fill="#e0241c"/></svg></div></div>
    <div class="photo-tile" style="left:205px;top:554px"><div class="photo-fill" role="img" aria-label="Portrait of a user by the water" style="background:linear-gradient(135deg,#9cc6dc,#dcc09a)"></div><div class="like-badge">123<svg viewBox="0 0 24 21"><path d="M12 21 2 11A6 6 0 0 1 12 3a6 6 0 0 1 10 8z" fill="#e0241c"/></svg></div></div>
    <div class="photo-tile" style="left:401px;top:554px"><div class="photo-fill" role="img" aria-label="Close portrait of a user with bold makeup" style="background:linear-gradient(135deg,#3a1e14,#b0683c 55%,#2a140c)"></div><div class="like-badge">123<svg viewBox="0 0 24 21"><path d="M12 21 2 11A6 6 0 0 1 12 3a6 6 0 0 1 10 8z" fill="#e0241c"/></svg></div></div>
  </section>

  <nav class="dock">
    <div class="dock-item" style="left:-2px">
      <svg width="30" height="40" viewBox="0 0 30 40"><path d="M15 2a12 12 0 0 1 12 12c0 9-12 20-12 20S3 23 3 14A12 12 0 0 1 15 2z" fill="#a3a5a6"/><circle cx="15" cy="14" r="4.5" fill="#2e2f30"/><ellipse cx="15" cy="37" rx="9" ry="2.5" fill="#a3a5a6"/></svg>
      <span class="dock-label">Feed</span>
    </div>
    <div class="dock-item is-active" style="left:112px">
      <svg width="48" height="38" viewBox="0 0 48 38"><g fill="#e0241c"><circle cx="10" cy="9" r="5.5"/><circle cx="38" cy="9" r="5.5"/><path d="M1 30c0-9 3-14 9-14s9 5 9 14z"/><path d="M29 30c0-9 3-14 9-14s9 5 9 14z"/><circle cx="24" cy="10" r="7"/><path d="M12 36c0-11 4-17 12-17s12 6 12 17z"/></g></svg>
      <span class="dock-label">People</span>
    </div>
    <div class="dock-item" style="left:372px">
      <svg width="44" height="40" viewBox="0 0 44 40"><path d="M4 2h36a3 3 0 0 1 3 3v24a3 3 0 0 1-3 3H27l-5 7-5-7H4a3 3 0 0 1-3-3V5a3 3 0 0 1 3-3z" fill="#a3a5a6"/><path d="M22 26 14 18a4.5 4.5 0 0 1 8-5 4.5 4.5 0 0 1 8 5z" fill="#2e2f30"/></svg>
      <span class="dock-label">Activity</span>
    </div>
    <div class="dock-item" style="left:484px">
      <svg width="40" height="40" viewBox="0 0 40 40"><circle cx="20" cy="12" r="10" fill="#a3a5a6"/><path d="M15 12a2 2 0 0 0 10 0z" fill="#2e2f30"/><path d="M4 38c0-10 7-15 16-15s16 5 16 15z" fill="#a3a5a6"/></svg>
      <span class="dock-label">Me</span>
    </div>
  </nav>
  <div class="camera-button">
    <svg width="60" height="46" viewBox="0 0 60 46"><path d="M6 9h12l4-7h16l4 7h12a4 4 0 0 1 4 4v27a4 4 0 0 1-4 4H6a4 4 0 0 1-4-4V13a4 4 0 0 1 4-4z" fill="#8d9091"/><circle cx="30" cy="26" r="12" fill="#2e2f30"/><path d="M30 19v14M23 26h14" stroke="#8d9091" stroke-width="3" stroke-linecap="round"/></svg>
  </div>
  <div class="notice-badge">1</div>
</main>
</body>
</html>
```